Desktop and Networking Support Course 9.17.25

Important the ad should not be very busy with the text taking up the major part of the ad .. please do not make the text so big that it takes up most of the ad..
Flyer Design Brief for Graphic Artist
also i am looking for something unique or creative that it will stand out .
Size & Layout:
Full Page with Bleed: 8” x 10.75” + 0.25” bleed on all sides.
Footer Space: Leave a 1-inch margin at the bottom for footer content (e.g., contact info, logo, or call-to-action).
Target Audience:
College-age students (around 24 years old)
Located in the USA
Interested in creative, professional, and career-building opportunities
Purpose:
To attract students to enroll in a college program
Flyer should be eye-catching, unique, and creative
Text must be clear and readable,
Design Style:
Use vector art, typography, or photography — your choice
If using photography, feature a white young professional USA citizen:
Wearing a white collared shirt
not with long hair
Creative Direction:
The flyer should stand out visually — something people would want to look at and keep
Showcase creativity and professionalism
Use bold colors, dynamic layout, or unexpected design elements to grab attention
Avoid clutter — keep the design balanced and clean
Text Suggestions (can be adjusted):
Footer,
please leave one inch on the bottom for the footer

```html
<!DOCTYPE html>
<html lang="en">
<head>
<meta charset="utf-8">
<title>Desktop &amp; Network Support Course</title>
<link rel="stylesheet" href="https://fonts.googleapis.com/css2?family=Archivo:ital,wght@0,600;0,700;0,800;1,700;1,800&family=Poppins:wght@700;800&family=Roboto+Slab:wght@600&display=swap">
<style>
  :root {
    --blue-deep: #0a4fe0;
    --blue-mid: #1a7fee;
    --blue-bright: #2a9af5;
    --navy: #0000b0;
    --navy-strip: #18248a;
    --cyan: #12f0f0;
    --white: #ffffff;
    --panel: rgba(110, 190, 245, 0.55);
    --footer: #0a86e0;
    --footer-top: #1b6ea8;
  }
  * { margin: 0; padding: 0; box-sizing: border-box; }
  html, body { width: 907px; height: 1200px; overflow: hidden; background: var(--blue-deep); }
  .flyer {
    position: relative;
    width: 907px;
    height: 1200px;
    overflow: hidden;
    background: linear-gradient(160deg, var(--blue-deep) 0%, var(--blue-mid) 55%, var(--blue-bright) 100%);
    font-family: "Archivo", Arial, sans-serif;
    color: var(--white);
  }
  .shapes { position: absolute; inset: 0; width: 907px; height: 1200px; }
  .trim-frame {
    position: absolute; left: 27px; top: 26px; width: 853px; height: 1148px;
    border: 1.5px dashed rgba(255,255,255,0.85);
    z-index: 5;
  }
  .course-label {
    position: absolute; top: 46px; left: 0; width: 907px; text-align: center;
    font-weight: 800; font-size: 17px; letter-spacing: 6.2px;
  }
  .headline {
    position: absolute; top: 96px; left: 60px; width: 790px;
    font-family: "Poppins", Arial, sans-serif; font-weight: 800;
    font-size: 113px; line-height: 1; letter-spacing: -1px; white-space: nowrap;
  }
  .subline {
    position: absolute; top: 219px; left: 74px;
    font-family: "Archivo", Arial, sans-serif; font-weight: 700;
    font-size: 36px; letter-spacing: -0.8px; white-space: nowrap;
  }
  .portrait { position: absolute; z-index: 1; }
  .mastery { position: absolute; left: 509px; top: 336px; width: 336px; }
  .spread { display: flex; justify-content: space-between; line-height: 1; }
  .spread.master { font-family: "Roboto Slab", Georgia, serif; font-weight: 600; font-size: 48px; color: var(--cyan); }
  .spread.product { font-family: "Archivo", Arial, sans-serif; font-weight: 800; font-size: 45px; margin-top: 15px; }
  .os-line { font-weight: 700; font-size: 33px; letter-spacing: -1.2px; margin-top: 8px; white-space: nowrap; line-height: 1; }
  .stat {
    position: absolute; right: 59px; top: 540px; text-align: right;
    font-weight: 800; font-size: 39px; line-height: 1.12; letter-spacing: -0.3px; z-index: 3;
  }
  .ranking {
    position: absolute; right: 59px; top: 697px; text-align: right;
    font-style: italic; font-weight: 800; font-size: 20px; line-height: 1.28; z-index: 3;
  }
  .benefits { position: absolute; left: 48px; top: 803px; list-style: none; z-index: 3; }
  .benefits li {
    display: flex; align-items: center; height: 41.5px;
    font-weight: 700; font-size: 29px; letter-spacing: -0.2px; white-space: nowrap;
  }
  .benefits li::before {
    content: ""; width: 26px; height: 21px; background: var(--cyan); margin-right: 14px; flex: none;
  }
  .options {
    position: absolute; right: 61px; top: 970px; text-align: right;
    font-weight: 700; font-size: 21px; line-height: 1.22; z-index: 3;
  }
  .footer-zone { position: absolute; left: 0; top: 1068px; width: 907px; height: 106px; background: var(--footer); }
  .edge-strip { position: absolute; left: 0; top: 1174px; width: 907px; height: 26px; background: var(--navy-strip); }
</style>
</head>
<body>
<main class="flyer">
  <svg class="shapes" viewBox="0 0 907 1200" aria-hidden="true">
    <polygon points="907,478 690,695 690,1035 907,1035" fill="#2636d6" opacity="0.75"/>
    <rect x="0" y="1034" width="907" height="34" fill="var(--footer-top)"/>
  </svg>

  <div class="portrait" role="img" aria-label="Photo of a smiling young professional with a short bob, wearing a white collared shirt and holding a laptop"
       style="left:33px; top:375px; width:396px; height:659px; border-radius:180px 180px 0 0; background:linear-gradient(180deg, #a7744a 0%, #d8a98a 30%, #f2f2f2 55%, #e8ecf2 100%); opacity:0.95;"></div>

  <svg class="shapes" viewBox="0 0 907 1200" style="z-index:2" aria-hidden="true">
    <polygon points="429,700 725,694 677,939 400,945" fill="#3a3c44" role="img" aria-label="Laptop held open"/>
    <polygon points="3,765 705,765 673,925 0,999" fill="var(--panel)"/>
    <rect x="0" y="1001" width="464" height="9" fill="var(--navy)"/>
    <polygon points="475,958 907,917 907,1034 458,1034" fill="var(--navy)"/>
    <polygon points="208,276 296,247 266,332 251,290" fill="var(--white)"/>
  </svg>

  <div class="trim-frame"></div>

  <p class="course-label">DESKTOP &amp; NETWORK SUPPORT COURSE</p>
  <h1 class="headline">YOUR CAREER</h1>
  <p class="subline">IS JUST A CLICK AWAY</p>

  <div class="mastery">
    <div class="spread master"><span>M</span><span>A</span><span>S</span><span>T</span><span>E</span><span>R</span></div>
    <div class="spread product"><span>S</span><span>K</span><span>Y</span><span>P</span><span>A</span><span>N</span><span>E</span></div>
    <p class="os-line">OPERATING SYSTEMS</p>
  </div>

  <p class="stat">90% Employment Rate –<br>CLASS OF 2024</p>
  <p class="ranking">Prepare for 3 of the Top 10 Tech Jobs<br>National Career Review 2025</p>

  <ul class="benefits">
    <li>Hands-On Desktop &amp; Network Training</li>
    <li>Real-World Troubleshooting Skills</li>
    <li>Ready for IT Jobs</li>
  </ul>

  <p class="options">In-Person and Remote Options<br>Partial Scholarships Offered</p>

  <div class="footer-zone"></div>
  <div class="edge-strip"></div>
</main>
</body>
</html>
```